Yoga Studio - Class Timetable Flyer

We require a double sided, size DL (1/3 A4) flyer with our class timetable included.
We would like the final flyer to have.
Side A : Yoga image, logo, address, website, contact phone number, and in big font $40 Introductory Month.
Side B: Clear easy to read timetable, class descriptions and website.
Thank you.
Yours kindly,
Nadia
87d0c7
86cae7
85acd3

```html
<!DOCTYPE html>
<html lang="en">
<head>
<meta charset="utf-8">
<title>Stillwater Studio – Class Timetable Flyer</title>
<link href="https://fonts.googleapis.com/css2?family=Arimo:wght@400;700&family=Questrial&display=swap" rel="stylesheet">
<style>
  :root {
    --page-bg: #e9e9eb;
    --teal-deep: #0c4553;
    --teal-mid: #1d6c7b;
    --teal-glow: #7fe3e2;
    --white: #ffffff;
    --cell-empty: #3e7a89;
    --cell-time: #1e4e5f;
    --cell-corner: #2b6479;
    --ink: #16262c;
    --mon: #7ee9f1;
    --tue: #f27ddb;
    --wed: #c9a1f1;
    --thu: #a9e14d;
    --fri: #f28b12;
    --sat: #62e9a9;
    --sun: #f8b263;
    --star: #ffe01a;
  }
  * { margin: 0; padding: 0; box-sizing: border-box; }
  html, body { width: 1200px; height: 914px; overflow: hidden; }
  body { background: var(--page-bg); position: relative; font-family: "Arimo", Arial, sans-serif; }

  /* ---------- Side A ---------- */
  .side-a {
    position: absolute; left: 36px; top: 32px; width: 848px; height: 423px;
    background: radial-gradient(ellipse 420px 300px at 540px 230px, var(--teal-glow) 0%, #3aa6ae 40%, var(--teal-mid) 70%, var(--teal-deep) 100%);
    overflow: hidden;
    font-family: "Questrial", "Century Gothic", sans-serif;
    color: var(--white);
  }
  .hero-photo {
    position: absolute; left: 300px; top: 28px; width: 440px; height: 360px;
    border-radius: 50% 50% 40% 40%;
    background: radial-gradient(ellipse at 50% 55%, rgba(215,250,248,.55) 0%, rgba(120,215,220,.35) 45%, rgba(60,150,165,0) 75%);
  }
  .brand { position: absolute; left: 50px; top: 108px; width: 220px; text-align: center; }
  .brand-dot { width: 58px; height: 58px; border-radius: 50%; background: var(--white); margin: 0 auto 18px; }
  .brand-name { font-size: 42px; line-height: 1; letter-spacing: 1px; }
  .brand-sub { font-size: 15px; letter-spacing: 6px; margin-top: 6px; }
  .brand-tag { font-size: 9.5px; letter-spacing: 1px; margin-top: 5px; }
  .intro-offer {
    position: absolute; right: 28px; top: 26px; text-align: right; line-height: 1;
  }
  .intro-price { font-size: 64px; }
  .intro-label { font-size: 22px; margin-top: 4px; letter-spacing: .5px; }
  .contact-bar {
    position: absolute; left: 47px; top: 390px; display: flex; gap: 9px;
    font-size: 13.4px; white-space: nowrap;
  }
  .contact-bar .sep { opacity: .9; }

  /* ---------- Side B ---------- */
  .side-b {
    position: absolute; left: 315px; top: 448px; width: 848px; height: 424px;
    background: linear-gradient(160deg, #0f4452 0%, #17606f 45%, #2c8b95 80%, #5fc3c4 100%);
    overflow: hidden; color: var(--white);
  }
  .timetable {
    position: absolute; left: 21px; top: 20px;
    display: grid;
    grid-template-columns: 50px repeat(7, 50px);
    grid-template-rows: 32px repeat(6, 55px);
    column-gap: 3.6px; row-gap: 4px;
  }
  .timetable > div { font-size: 12px; line-height: 15px; color: var(--ink); }
  .corner { background: var(--cell-corner); }
  .day { display: flex; align-items: center; justify-content: center; font-size: 12.5px !important; }
  .time { background: var(--cell-time); color: var(--white) !important; display: flex; align-items: center; padding-left: 4px; }
  .empty { background: var(--cell-empty); }
  .class { padding: 4px 2px 0 3px; letter-spacing: -.2px; }
  .class.tight { letter-spacing: -.8px; }
  .mon { background: var(--mon); } .tue { background: var(--tue); } .wed { background: var(--wed); }
  .thu { background: var(--thu); } .fri { background: var(--fri); } .sat { background: var(--sat); }
  .sun { background: var(--sun); }
  .class .star { color: var(--star); font-size: 16px; line-height: 12px; }

  .divider { position: absolute; left: 451px; top: 10px; height: 404px; border-left: 1px dashed rgba(255,255,255,.45); }
  .descriptions { position: absolute; left: 480px; top: 24px; width: 360px; font-size: 12.5px; line-height: 16.4px; }
  .descriptions p { margin-bottom: 7px; }
  .descriptions .star { position: absolute; left: -21px; top: 49px; color: var(--star); font-size: 19px; }
  .side-b-web { position: absolute; left: 480px; top: 346px; font-size: 13px; font-weight: 700; letter-spacing: .3px; }
  .footnotes { position: absolute; left: 463px; top: 374px; font-size: 9px; line-height: 10.5px; opacity: .85; }
</style>
</head>
<body>

<section class="side-a">
  <div class="hero-photo" role="img" aria-label="Photo of two women practising yoga, one seated cross-legged, one in upward dog pose, on a glowing teal backdrop"></div>
  <div class="brand">
    <div class="brand-dot"></div>
    <div class="brand-name">stillwater</div>
    <div class="brand-sub">STUDIO</div>
    <div class="brand-tag">YOGA • FITNESS • AQUA</div>
  </div>
  <div class="intro-offer">
    <div class="intro-price">$40</div>
    <div class="intro-label">Introductory Month</div>
  </div>
  <div class="contact-bar">
    <span>24 Wattle Crescent, Greenvale, Vic, 3059</span><span class="sep">|</span>
    <span>www.stillwaterstudio.com.au</span><span class="sep">|</span>
    <span>nadiakerrigan@mailbox.com</span><span class="sep">|</span>
    <span>0491 570 156</span>
  </div>
</section>

<section class="side-b">
  <div class="timetable">
    <div class="corner"></div>
    <div class="day mon">Mon</div><div class="day tue">Tues</div><div class="day wed">Wed</div>
    <div class="day thu">Thurs</div><div class="day fri">Fri</div><div class="day sat">Sat</div><div class="day sun">Sun</div>

    <div class="time">9.30am</div>
    <div class="empty"></div>
    <div class="class tue">Hot<br>90mins</div>
    <div class="empty"></div>
    <div class="class thu">Power<br>Vinyasa<br>75mins</div>
    <div class="empty"></div>
    <div class="class sat">Power<br>Vinyasa<br>90mins</div>
    <div class="empty"></div>

    <div class="time">11am</div>
    <div class="empty"></div><div class="empty"></div><div class="empty"></div>
    <div class="class thu tight">Power<br>Essentials<br>60 mins</div>
    <div class="empty"></div><div class="empty"></div><div class="empty"></div>

    <div class="time">1pm</div>
    <div class="empty"></div><div class="empty"></div>
    <div class="class wed">Hot<br>90mins</div>
    <div class="empty"></div><div class="empty"></div><div class="empty"></div><div class="empty"></div>

    <div class="time">4.30pm</div>
    <div class="empty"></div><div class="empty"></div><div class="empty"></div>
    <div class="empty"></div><div class="empty"></div><div class="empty"></div>
    <div class="class sun">Power<br>Vinyasa<br>90mins</div>

    <div class="time">6.30pm</div>
    <div class="class mon">Power<br>Vinyasa<br>60mins</div>
    <div class="empty"></div>
    <div class="class wed">Hot<br>60mins</div>
    <div class="empty"></div>
    <div class="class fri">Funky<br>Flow<span class="star">★</span><br>75mins</div>
    <div class="empty"></div>
    <div class="class sun">Yin<br>60mins</div>

    <div class="time">7.45pm</div>
    <div class="class mon tight">Power<br>Essentials<br>60mins</div>
    <div class="empty"></div>
    <div class="class wed">Power<br>Vinyasa<br>60mins</div>
    <div class="empty"></div><div class="empty"></div><div class="empty"></div><div class="empty"></div>
  </div>

  <div class="divider"></div>

  <div class="descriptions">
    <span class="star">★</span>
    <p>Funky Flow:<br>Finish off the week and head into the weekend with a joyful flowing class to a playlist of funky beats.<br>Charity class by donation, suggested $10. Please place cash only in the charity donation box. Frequent guest teachers.</p>
    <p>Hot:<br>Dynamic sequence of Strength and Breathing exercises. Suitable for beginners. Heat 37 = degrees.</p>
    <p>Power Essentials:<br>Flowing Practice with space and time to Align and understand the poses deeply, building muscular strength and endurance. Ideal for beginners.</p>
    <p>Power Vinyasa:<br>Strong, Dynamic, Flowing practice ideal for building physical power, flexibility and mental resilience. Heat = 30 degrees</p>
    <p>Yin:<br>Long, Slow, Deep practice with a focus on supporting the body to release our deep internal structures of connective tissue.</p>
  </div>

  <div class="side-b-web">www.stillwaterstudio.com.au</div>

  <div class="footnotes">
    •Introductory Month only available to first time members.<br>
    •Please present concession card and ID for concession prices.<br>
    &nbsp;&nbsp;Available to full-time students only
  </div>
</section>

</body>
</html>
```